Visitenkarten/Briefpaier/Kassenkassenbelege für Juwelier
Zielgruppe
Mittelständischer Juwelier mit zwei Filialen. Klassischer Schmuck, Uhren und Modeschmuck
Aufgabenstellung
Es müssen für zwei Geschäfte Visitenkarten, Briefpapier (A4) und Kassenkassenbelege (A6) erstellt werden. Logo und fenwiro im Anhang. Ein Farbkonzept besteht noch nicht. Die Idee geht in Richtung Bordeaux-Rot.
Generell:
(1) Sieht erstmal nach viel Beschreibung aus, bitte nicht entmutigen lassen, sind zu 90% nur austauschbare Inhalts-/Kontaktdaten.
(2) Für meine Zwecke reicht es vollkommen aus, wenn bei den Vorschlägen zur Arbeitsersparnis erstmal nur mit einer Adresse gearbeitet wird. Wenn ich dann den zutreffenden Designvorschlag gefunden habe, können wir die zweite Adresse in dem ersten Format umsetzen. Ich denke das spart Zeit und Nerven.
(3) Bitte Angaben wie "Tel.:" oder "USt.- ID:" nicht wörtlich nehmen, es soll dabei klar sein worum es geht; wenn "Telefon" ausgeschrieben besser aussieht, bitte in der optisch ansprechenderen Form verwenden.
(4) Bei Fragen, bitte fragen!
(5) Viel Spass bei dem Projekt - Ich freu' mich auf die Vorschläge!
Visitenkarten(1):
Juwelier Brandauer GmbH
www.juwelier-brandauer-example.de
Visitenkarten(2):
Visitenkarten(generell):
(1) Die einzelnen Daten können durch Hervorhebungen wie Adresse, Kontakt, Online/Internet unterteilt bzw. hervorgehoben werden.
(2) Die Visitenkarten sollen farbig gedruckt werden; geplant ist weiß als Hintergrund ist aber nicht zwingend bei einer guten anderen Idee
Briefpapier:
(1)Absender im Adressfeld für DIN-lang Briefumschläge mit Fenster:
(2)Informationen im Footer/Seitenbereich:
Juwelier Brandauer Gmb..

```html
<!DOCTYPE html>
<html lang="de">
<head>
<meta charset="utf-8">
<title>Juwelier Brandauer – Briefpapier und Umschlag</title>
<link rel="stylesheet" href="https://fonts.googleapis.com/css2?family=Source+Sans+3:wght@400;600;700&family=Arimo:wght@400&display=swap">
<style>
  :root {
    --stage: #f7f7f7;
    --paper: #ffffff;
    --red-deep: #cc1117;
    --red: #e2231a;
    --orange: #e8572a;
    --ink: #4a4440;
    --grey-text: #555555;
    --mark: #888888;
  }
  * { margin: 0; padding: 0; box-sizing: border-box; }
  html, body { width: 1200px; height: 1000px; overflow: hidden; background: var(--stage); }
  .canvas { position: relative; width: 1200px; height: 1000px; }

  .crop { position: absolute; background: var(--mark); }
  .crop.v { width: 1px; height: 26px; }
  .crop.h { height: 1px; width: 26px; }

  .sheet {
    position: absolute; background: var(--paper);
    box-shadow: 2px 3px 6px rgba(0,0,0,.18);
    overflow: hidden;
  }
  .bottom-band {
    position: absolute; left: 0; right: 0; bottom: 0; height: 6px;
    background: linear-gradient(90deg, var(--red-deep), var(--orange) 50%, var(--red));
  }

  /* Name block: plain circle + invented name */
  .brand { position: absolute; display: flex; align-items: center; gap: 8px; }
  .brand-dot { flex: none; border-radius: 50%; background: var(--red); }
  .brand-name {
    font-family: "Source Sans 3", sans-serif; font-weight: 400;
    color: var(--ink); white-space: nowrap;
  }

  /* Letterhead */
  .letterhead { left: 42px; top: 50px; width: 533px; height: 753px; }
  .letterhead .brand { left: 58px; top: 70px; }
  .letterhead .brand-dot { width: 12px; height: 12px; }
  .letterhead .brand-name { font-size: 20px; }

  .address-field { position: absolute; left: 25px; top: 128px; width: 228px; height: 89px; }
  .corner { position: absolute; width: 12px; height: 12px; border-color: var(--mark); border-style: solid; border-width: 0; }
  .corner.tl { left: 0; top: 0; border-top-width: 1px; border-left-width: 1px; }
  .corner.tr { right: 0; top: 0; border-top-width: 1px; border-right-width: 1px; }
  .corner.bl { left: 0; bottom: 0; border-bottom-width: 1px; border-left-width: 1px; }
  .corner.br { right: 0; bottom: 0; border-bottom-width: 1px; border-right-width: 1px; }
  .recipient {
    font-family: "Arimo", sans-serif; font-size: 8px; line-height: 12px; color: var(--grey-text);
  }
  .address-field .recipient { position: absolute; left: 36px; top: 17px; }

  .fold-mark { position: absolute; left: 0; width: 18px; height: 1px; background: #cccccc; }

  .info-panel {
    position: absolute; left: 389px; top: 0; width: 144px; height: 379px;
    background: linear-gradient(90deg, var(--red-deep), var(--red));
    color: #ffffff; font-family: "Source Sans 3", sans-serif;
    padding: 41px 0 0 13px;
  }
  .info-panel .company { font-size: 10px; font-weight: 600; line-height: 12px; }
  .info-panel .block { font-size: 7.3px; line-height: 10.8px; margin-bottom: 10px; }
  .info-panel .block.fine { font-size: 6px; line-height: 8px; margin-bottom: 10px; }
  .info-panel .block.branch { font-size: 7.3px; line-height: 8.3px; margin-top: 2px; }

  /* Envelope front */
  .envelope-front { left: 623px; top: 100px; width: 558px; height: 286px; }
  .sender { position: absolute; left: 34px; top: 26px; font-family: "Source Sans 3", sans-serif; }
  .sender .company { color: var(--red); font-size: 9.5px; font-weight: 700; line-height: 12px; }
  .sender .line { color: var(--grey-text); font-size: 7.3px; line-height: 11px; }
  .window {
    position: absolute; left: 38px; top: 153px; width: 224px; height: 90px;
    border-radius: 8px; border: 1px solid #e4e4e4;
    box-shadow: inset 2px 2px 2px rgba(0,0,0,.25);
  }
  .window .recipient { position: absolute; left: 39px; top: 22px; }
  .envelope-front .brand { left: 382px; top: 210px; }
  .envelope-front .brand-dot { width: 10px; height: 10px; }
  .envelope-front .brand-name { font-size: 17px; }

  /* Envelope back */
  .envelope-back { left: 623px; top: 475px; width: 558px; height: 285px; }
  .flap { position: absolute; left: 0; top: 0; }
  .envelope-back .brand { left: 222px; top: 22px; gap: 6px; }
  .envelope-back .brand-dot { width: 8px; height: 8px; }
  .envelope-back .brand-name { font-size: 12px; }
</style>
</head>
<body>
<div class="canvas">

  <div class="crop v" style="left:42px; top:12px;"></div>
  <div class="crop v" style="left:575px; top:12px;"></div>
  <div class="crop v" style="left:42px; top:816px;"></div>
  <div class="crop v" style="left:575px; top:816px;"></div>
  <div class="crop h" style="left:4px; top:50px;"></div>
  <div class="crop h" style="left:588px; top:50px;"></div>
  <div class="crop h" style="left:4px; top:803px;"></div>
  <div class="crop h" style="left:588px; top:803px;"></div>

  <section class="sheet letterhead">
    <div class="brand">
      <span class="brand-dot"></span>
      <span class="brand-name">Juwelier Brandauer</span>
    </div>

    <div class="address-field">
      <span class="corner tl"></span><span class="corner tr"></span>
      <span class="corner bl"></span><span class="corner br"></span>
      <div class="recipient">
        Marlene Vogt<br>Am Mühlbach 12<br>53700 Musterdorf<br>SCHWEIZ
      </div>
    </div>

    <div class="fold-mark" style="top:267px;"></div>
    <div class="fold-mark" style="top:520px;"></div>

    <aside class="info-panel">
      <div class="company">Juwelier Brandauer GmbH</div>
      <div class="block">Lindenhofstraße 24<br>45479 Musterstadt</div>
      <div class="block">Tel.: 0208-555013<br>Fax: 0208-555014<br>info@juwelier-brandauer-example.de<br>www.juwelier-brandauer-example.de</div>
      <div class="block fine">Bankverbindung:<br>Beispielbank AG Essen<br>IBAN: DE00 1234 5678 9012 3456 78<br>BIC: BSPB DE 00</div>
      <div class="block fine">Steuernummer:<br>000/0000/0000<br>USt.- ID: DE 000000000</div>
      <div class="block branch">Filiale:<br>Kirchplatz 8<br>45527 Beispielheim</div>
    </aside>

    <div class="bottom-band"></div>
  </section>

  <section class="sheet envelope-front">
    <div class="sender">
      <div class="company">Juwelier Brandauer GmbH</div>
      <div class="line">Lindenhofstraße 24</div>
      <div class="line">45479 Musterstadt</div>
    </div>
    <div class="window">
      <div class="recipient">
        Marlene Vogt<br>Am Mühlbach 12<br>53700 Musterdorf<br>SCHWEIZ
      </div>
    </div>
    <div class="brand">
      <span class="brand-dot"></span>
      <span class="brand-name">Juwelier Brandauer</span>
    </div>
    <div class="bottom-band"></div>
  </section>

  <section class="sheet envelope-back">
    <svg class="flap" width="558" height="70" viewBox="0 0 558 70" aria-hidden="true">
      <path d="M0 2 L28 52 Q34 62 48 62 L500 62 Q514 62 522 54 L558 4"
            fill="#ffffff" stroke="#d6d6d6" stroke-width="1"/>
      <path d="M28 63 L500 63" stroke="rgba(0,0,0,.07)" stroke-width="2"/>
    </svg>
    <div class="brand">
      <span class="brand-dot"></span>
      <span class="brand-name">Juwelier Brandauer</span>
    </div>
  </section>

</div>
</body>
</html>
```